Varotesk with two other company logos

We need a new design for our business cards. We have used the same business cards for more than 10 years. We have now expanded and want to add our other two business logos to incorporate with our original business logo. I have added our current business card (Varotesk) onto here. Also I have added an example of what we would like to see on the business card.

Target Market(s)

Nutritional market

Industry/Entity Type

Business

Contact Information for Business Card

Varotesk, Hallinger Product Plant, Brisk lift Product
Will use business cards for Multiple of people in my company.

Colors

Designer to choose colors to be used in the design.

Requirements
Must have
• three logos on my business cards
Nice to have
• something that stands out.

```html
<!DOCTYPE html>
<html lang="en">
<head>
<meta charset="utf-8">
<title>Varotesk Business Cards</title>
<link rel="stylesheet" href="https://fonts.googleapis.com/css2?family=Montserrat:wght@400;500;600;700&display=swap">
<style>
  :root {
    --bg: #d4d4d4;
    --card: #ffffff;
    --green: #7ba05b;
    --purple: #5a1f5f;
    --navy: #1f2f7a;
    --yellow: #d9c400;
    --pink: #e0457b;
    --ink: #1a1a1a;
    --leaf: #f1f2f0;
  }
  * { margin: 0; padding: 0; box-sizing: border-box; }
  html, body { width: 1200px; height: 800px; overflow: hidden; background: var(--bg); }
  body { position: relative; font-family: "Montserrat", Arial, sans-serif; }

  .card {
    position: absolute;
    width: 560px; height: 320px;
    background: var(--card);
    box-shadow: 0 4px 14px rgba(0,0,0,.18);
    overflow: hidden;
  }
  .card--front { left: 27px; top: 60px; }
  .card--hallinger { left: 613px; top: 60px; }
  .card--brisk { left: 320px; top: 420px; }

  /* front */
  .brand {
    position: absolute; right: 40px; top: 44px;
    display: flex; align-items: center; gap: 10px;
  }
  .brand__dot { width: 14px; height: 14px; border-radius: 50%; background: var(--pink); }
  .brand__name { font-size: 36px; font-weight: 500; color: var(--ink); letter-spacing: 2px; }

  .person { position: absolute; left: 34px; top: 150px; }
  .person__name { font-size: 25px; font-weight: 500; color: var(--green); letter-spacing: .5px; }
  .person__role { font-size: 12px; font-weight: 500; color: var(--purple); margin-top: 2px; letter-spacing: .5px; }

  .divider { position: absolute; left: 34px; right: 34px; top: 205px; height: 2px; background: var(--purple); }

  .contacts { position: absolute; left: 34px; top: 222px; list-style: none; }
  .contacts li { display: flex; align-items: center; gap: 12px; font-size: 15px; color: var(--purple); line-height: 23px; }
  .contacts svg { width: 11px; height: 11px; fill: var(--green); flex: none; }

  .address { position: absolute; right: 34px; top: 222px; font-size: 14px; color: var(--purple); line-height: 21px; text-align: left; }

  /* backs */
  .leaf-glow {
    position: absolute; left: 150px; top: -10px; width: 300px; height: 340px;
    border-radius: 50%;
    background: radial-gradient(ellipse at center, var(--leaf) 0%, rgba(241,242,240,.6) 55%, rgba(255,255,255,0) 75%);
  }
  .mark {
    position: absolute; left: 0; right: 0; top: 50%; transform: translateY(-50%);
    display: flex; flex-direction: column; align-items: center; gap: 6px;
  }
  .mark__row { display: flex; align-items: center; gap: 10px; }
  .mark__dot { width: 16px; height: 16px; border-radius: 50%; }
  .mark--hallinger .mark__dot { background: var(--pink); }
  .mark--brisk .mark__dot { background: var(--navy); }
  .mark__name { font-size: 36px; font-weight: 700; letter-spacing: 1px; }
  .mark--hallinger .mark__name { color: var(--green); }
  .mark--brisk .mark__name { color: var(--navy); font-size: 28px; }
  .mark__sub { font-size: 15px; font-weight: 400; letter-spacing: 3px; }
  .mark--hallinger .mark__sub { color: var(--green); }
  .mark--brisk .mark__sub { color: var(--yellow); font-weight: 600; font-size: 12px; }
</style>
</head>
<body>

  <section class="card card--front">
    <div class="brand">
      <span class="brand__dot"></span>
      <span class="brand__name">VAROTESK</span>
    </div>
    <div class="person">
      <div class="person__name">MARLO QUINT</div>
      <div class="person__role">DIRECTOR</div>
    </div>
    <div class="divider"></div>
    <ul class="contacts">
      <li><svg viewBox="0 0 12 12"><path d="M3 0l2 3-1.2 1.2c.6 1.5 1.6 2.5 3 3L8 6l3 2-1 3C5 11 1 7 1 2z"/></svg>+1.202.555.0143</li>
      <li><svg viewBox="0 0 12 12"><path d="M0 2h12v8H0zM1 3v.4l5 3.2 5-3.2V3z"/></svg>info@varotesk.com</li>
      <li><svg viewBox="0 0 12 12"><circle cx="6" cy="6" r="6"/></svg>www.varotesk.com</li>
    </ul>
    <div class="address">418 Alder Row, Ste 3B<br>Linden, GA 30999 - 4120</div>
  </section>

  <section class="card card--hallinger">
    <div class="leaf-glow" role="img" aria-label="Faint large leaf decoration"></div>
    <div class="mark mark--hallinger">
      <div class="mark__row">
        <span class="mark__dot"></span>
        <span class="mark__name">HALLINGER</span>
      </div>
      <span class="mark__sub">PRODUCT PLANT</span>
    </div>
  </section>

  <section class="card card--brisk">
    <div class="mark mark--brisk">
      <div class="mark__row">
        <span class="mark__dot"></span>
        <span class="mark__name">BRISK LIFT PRODUCT</span>
      </div>
      <span class="mark__sub">STRENGTH FROM WITHIN</span>
    </div>
  </section>

</body>
</html>
```